Modern business card for triathlon training business in Australia

We need a business card design for our triathlon training company.

Pace with Us Fitness is an Australian business, owned by women, run for women. Pace with Us Fitness helps women prepare or improve triathlon skills and confidence through triathlon camps completely designed for women.

Our camps focus on preparing women both physically and mentally for their next (or first!) triathlon.

You can see our website www.pacewithusfitness.com.au for more info about our business and our style.

We've attached two of our logos and are happy to consider a design that utilised either colour scheme with the teal colour being our 'feature' colour. We don't want overly feminine cards but rather cards that are professional and neat. If the inclusion of any pictures/art is warranted, this should be focused on our swim/ride/run theme and in that specific order (swim/ride/run).

The business card needs to be a printable design and the contact details will need to change for our two employees.

Target Market(s)

Female clients and partners/vendors/sponsors that we work with in the triathlon industry

Industry/Entity Type

Fitness

Contact Information for Business Card

Pace with Us Fitness (business name)
Nina Carver
Business Director
Mobile: 0438 916 207
Email: nina@pacewithusfitness.com.au
www.pacewithusfitness.com.au

Second business card:
Pace with Us Fitness
Bel Stray
Coaching Director
Mobile: 0459 260 718
Email: bel@pacewithusfitness.com.au

Font styles to use
Serif
Sans Serif

Requirements
Must have
• Core contact details above, our logo and be a printable design
Should not have
• Pink
• Cursive/script fonts

```html
<!DOCTYPE html>
<html lang="en">
<head>
<meta charset="utf-8">
<title>Pace with Us Fitness – Business Cards</title>
<link rel="stylesheet" href="https://fonts.googleapis.com/css2?family=Cabin:ital,wght@0,400;0,600;0,700;1,400&display=swap">
<style>
  :root {
    --teal: #19bdd0;
    --teal-pale: #7fd6e1;
    --sport-fill: #d3eff4;
    --sport-depth: #5cc6d5;
    --ink-grey: #6f6f6f;
    --white: #ffffff;
    --band-grey: #e3e3e3;
    --backdrop: #000000;
  }
  * { margin: 0; padding: 0; box-sizing: border-box; }
  html, body {
    width: 1200px; height: 900px; overflow: hidden;
    background: var(--backdrop);
    font-family: "Cabin", "Gill Sans", sans-serif;
  }
  .sheet { position: relative; width: 1200px; height: 900px; }

  .card {
    position: absolute; width: 240px; height: 370px;
    background: var(--white); overflow: hidden;
  }
  .card--front-a { left: 328px; top: 33px; }
  .card--back-a  { left: 653px; top: 33px; }
  .card--front-b { left: 328px; top: 495px; }
  .card--back-b  { left: 653px; top: 495px; }

  /* Front: swim / ride / run */
  .discipline {
    position: absolute; left: 0; width: 240px; height: 99px;
    display: flex; align-items: center; justify-content: center;
    font-weight: 700; font-size: 64px; letter-spacing: 1px;
    color: var(--sport-fill);
    text-shadow: 1px 1px 0 var(--sport-depth), 2px 2px 0 var(--sport-depth), 3px 3px 0 var(--sport-depth);
    border-bottom: 1px solid #d6d6d6;
  }
  .discipline--swim { top: 0;   background: linear-gradient(100deg, var(--white) 20%, var(--band-grey) 100%); }
  .discipline--ride { top: 100px; background: linear-gradient(100deg, var(--band-grey) 0%, var(--white) 45%, var(--band-grey) 100%); }
  .discipline--run  { top: 201px; background: linear-gradient(100deg, var(--band-grey) 0%, var(--white) 55%, var(--band-grey) 100%); }

  .tagline-band {
    position: absolute; left: 0; top: 309px; width: 240px; height: 61px;
    background: var(--teal);
    display: flex; align-items: center; justify-content: center;
    color: var(--white); font-style: italic; font-size: 14px;
  }
  .card--front-b .tagline-band { top: 307px; height: 63px; border-top: 2px solid #1a1a1a; }

  /* Back: brand + contact */
  .brand-panel {
    position: absolute; left: 0; top: 0; width: 240px; height: 225px;
    background: var(--teal);
    display: flex; align-items: center; justify-content: center;
  }
  .brand-name {
    color: var(--teal-pale); font-weight: 700; font-size: 25px;
    line-height: 1.1; text-align: center; text-transform: uppercase;
    letter-spacing: 0.5px;
  }
  .contact { position: absolute; left: 16px; top: 240px; }
  .contact__name { font-weight: 700; font-size: 17px; color: var(--ink-grey); }
  .contact__role { font-size: 11px; color: var(--ink-grey); margin-top: 2px; }
  .contact__lines { list-style: none; margin-top: 22px; }
  .contact__lines li { font-size: 11.5px; color: var(--teal); line-height: 14.6px; }
</style>
</head>
<body>
<main class="sheet">

  <section class="card card--front-a">
    <div class="discipline discipline--swim">SWIM</div>
    <div class="discipline discipline--ride">RIDE</div>
    <div class="discipline discipline--run">RUN</div>
    <div class="tagline-band">Give it a go.</div>
  </section>

  <section class="card card--back-a">
    <div class="brand-panel"><p class="brand-name">Pace with Us<br>Fitness</p></div>
    <div class="contact">
      <h2 class="contact__name">Nina Carver</h2>
      <p class="contact__role">Business Director</p>
      <ul class="contact__lines">
        <li>nina@pacewithusfitness.com.au</li>
        <li>0438 916 207</li>
        <li>www.pacewithusfitness.com.au</li>
      </ul>
    </div>
  </section>

  <section class="card card--front-b">
    <div class="discipline discipline--swim">SWIM</div>
    <div class="discipline discipline--ride">RIDE</div>
    <div class="discipline discipline--run">RUN</div>
    <div class="tagline-band">Give it a go.</div>
  </section>

  <section class="card card--back-b">
    <div class="brand-panel"><p class="brand-name">Pace with Us<br>Fitness</p></div>
    <div class="contact">
      <h2 class="contact__name">Bel Stray</h2>
      <p class="contact__role">Coaching Director</p>
      <ul class="contact__lines">
        <li>bel@pacewithusfitness.com.au</li>
        <li>0459 260 718</li>
        <li>www.pacewithusfitness.com.au</li>
      </ul>
    </div>
  </section>

</main>
</body>
</html>
```